Timesheet Software Banner Ad for Cloudmere Plug Bazaar

We need two PNG images for our product on the Cloudmere Plug bazaar:
- 1200 x 300 (full tile banner) and
- 280 x 205 (banner image)
PNG only

Our product allows
- users to enter time spent on projects via Timesheet as well as enter any expenses for re-imbursement.
- the application includes project management to plan and capure the actual time and expenses.
- managers approve the time/expenses and users are re-imbursed and time information is sent to payroll.
- you can also create customers invoices for time spent and expenses incurred.

There are two editions one basic "Nimbo H&C" without invoicing and payroll and limited project management and "Nimbo Max" - the full suite.

We would need two sets - one for "Nimbo H&C" and one for "Nimbo Max" - maybe design for the full product and the basic could then derived.

Our web page http://www.velqino.example

Target Market(s)

Cloudmere users who are looking for Timesheet and Expense Management

Industry/Entity Type

Software

Requirements
Must have
• There are Cloudmere restrictions (attached)
- as little as possible text
- avoid flat white background

```html
<!DOCTYPE html>
<html lang="en">
<head>
<meta charset="utf-8">
<title>Velqino Nimbo banners</title>
<link rel="stylesheet" href="https://fonts.googleapis.com/css2?family=Questrial&family=Roboto:wght@500&display=swap">
<style>
  :root {
    --page: #ffffff;
    --tile: #e7e7e7;
    --ink: #111111;
    --mark: #3f86ad;
    --brush: #b9df97;
    --tagline: #3f7fab;
    --cloud: #aec4d6;
  }
  html, body {
    margin: 0;
    width: 1200px;
    height: 960px;
    overflow: hidden;
    background: var(--page);
  }
  .canvas { position: relative; width: 1200px; height: 960px; }

  .banner {
    position: absolute;
    overflow: hidden;
    background: radial-gradient(circle at 40% 40%, #ebebeb, var(--tile));
  }
  .banner .cloud {
    position: absolute;
    border-radius: 50%;
    background: radial-gradient(ellipse at 50% 55%, var(--cloud) 0%, rgba(174,196,214,0.55) 35%, rgba(231,231,231,0) 70%);
  }
  .brand { position: absolute; display: flex; align-items: center; }
  .brand-dot { border-radius: 50%; background: var(--mark); flex: none; }
  .brand-name {
    font-family: "Questrial", sans-serif;
    color: var(--ink);
    line-height: 1;
    white-space: nowrap;
  }
  .edition {
    position: absolute;
    background: var(--brush);
    border-radius: 40px 14px 40px 14px;
    font-family: "Questrial", sans-serif;
    color: var(--ink);
    text-align: center;
    white-space: nowrap;
  }
  .tagline {
    position: absolute;
    margin: 0;
    font-family: "Roboto", sans-serif;
    font-weight: 500;
    color: var(--tagline);
  }

  /* small tile 280 x 205 */
  .banner--tile { width: 267px; height: 196px; top: 36px; }
  .banner--tile.tile-max { left: 284px; }
  .banner--tile.tile-hc { left: 754px; }
  .banner--tile .cloud { left: 120px; top: 40px; width: 160px; height: 110px; }
  .banner--tile .brand { left: 34px; top: 27px; gap: 8px; }
  .banner--tile .brand-dot { width: 34px; height: 34px; }
  .banner--tile .brand-name { font-size: 36px; }
  .banner--tile .edition { left: 104px; top: 66px; width: 118px; height: 22px; line-height: 22px; font-size: 20px; }
  .banner--tile .tagline { left: 0; width: 276px; top: 126px; font-size: 16.5px; line-height: 23px; text-align: center; }

  /* full tile 1200 x 300 */
  .banner--wide { width: 1146px; height: 287px; left: 27px; }
  .banner--wide.wide-max { top: 299px; }
  .banner--wide.wide-hc { top: 632px; }
  .banner--wide .cloud { left: 680px; top: 20px; width: 420px; height: 190px; }
  .banner--wide .brand { left: 78px; top: 44px; gap: 22px; }
  .banner--wide .brand-dot { width: 100px; height: 100px; }
  .banner--wide .brand-name { font-size: 104px; }
  .banner--wide .edition { left: 292px; top: 148px; width: 290px; height: 40px; line-height: 40px; font-size: 44px; }
  .banner--wide .tagline { left: 452px; top: 214px; font-size: 36px; line-height: 40px; white-space: nowrap; }
</style>
</head>
<body>
<main class="canvas">

  <section class="banner banner--tile tile-max">
    <div class="cloud" role="img" aria-label="Soft blue-grey cloud illustration"></div>
    <div class="brand"><span class="brand-dot"></span><span class="brand-name">Velqino</span></div>
    <div class="edition">Nimbo Max</div>
    <p class="tagline">Time and expense<br>tracking software</p>
  </section>

  <section class="banner banner--tile tile-hc">
    <div class="cloud" role="img" aria-label="Soft blue-grey cloud illustration"></div>
    <div class="brand"><span class="brand-dot"></span><span class="brand-name">Velqino</span></div>
    <div class="edition">Nimbo H&amp;C</div>
    <p class="tagline">Time and expense<br>tracking software</p>
  </section>

  <section class="banner banner--wide wide-max">
    <div class="cloud" role="img" aria-label="Soft blue-grey cloud illustration"></div>
    <div class="brand"><span class="brand-dot"></span><span class="brand-name">Velqino</span></div>
    <div class="edition">Nimbo Max</div>
    <p class="tagline">Time and expense tracking software</p>
  </section>

  <section class="banner banner--wide wide-hc">
    <div class="cloud" role="img" aria-label="Soft blue-grey cloud illustration"></div>
    <div class="brand"><span class="brand-dot"></span><span class="brand-name">Velqino</span></div>
    <div class="edition">Nimbo H&amp;C</div>
    <p class="tagline">Time and expense tracking software</p>
  </section>

</main>
</body>
</html>
```